VELO Selfie Wall Design for Coworking Space

Design a striking, large-scale wall mural for VELO Hub that embodies our brand identity, incorporates Oakland-inspired elements, and enhances our coworking and event space. The design should be bold, visually engaging, and aligned with our brand aesthetic—featuring black, white, and bronze tones.
Key Requirements:
Branded Mural Design
Prominently (but tastefully) feature the VELO Hub logo.
Use abstract shapes, gradients, or geometric patterns (inspired by the VELO logo) to convey movement and connectivity.
Incorporate the tagline: “Live · Work · Play · Go” in brand-approved typography.
Avoid literal imagery—keep the design sleek and modern.
Integrated Selfie Wall
Designate a photo-friendly zone with:
Open negative space (clean background) for people to pose naturally.
A bold but simple focal point (e.g., stylized typography, an Oakland-inspired icon, or a bronze metallic accent).
Lighting-friendly elements (avoid small patterns that may clash on camera).
Oakland Nods
Subtle references to the city (e.g., abstract skyline, bridge motifs, or topographic patterns) without being literal.
Updates
After reviewing designs, management has asked that this design incorporates a "selfie" aspect where people would be encouraged to take a photo with the wall. This would leave a thoughtful area for people to pose or engage with the design on the wall. Ideally, we want people to see the wall and take a picture with the design as a background
Target Market(s)
Office Employees
Industry/Entity Type
Real Estate/Coworking
Font styles to use
Other font styles liked:
- Henderson Sans
Look and feel
Each slider illustrates characteristics of the customer's brand and the style your logo design should communicate.

```html
<!DOCTYPE html>
<html lang="en">
<head>
<meta charset="utf-8">
<title>VELO Hub – Selfie Wall Mural</title>
<link href="https://fonts.googleapis.com/css2?family=Montserrat:wght@700&display=swap" rel="stylesheet">
<style>
  :root {
    --page: #ffffff;
    --wall: #ffffff;
    --teal: #034457;
    --bronze: #d59a64;
    --sweep-light: #e9ab74;
    --sweep-mid: #c9b9a8;
    --sweep-cool: #8fb0ba;
    --logo-dot: #c98552;
    --logo-text: #ffffff;
  }
  html, body {
    margin: 0;
    padding: 0;
    width: 935px;
    height: 1200px;
    overflow: hidden;
    background: var(--page);
  }
  .canvas {
    position: relative;
    width: 935px;
    height: 1200px;
  }
  .mural {
    position: absolute;
    left: 20px;
    top: 411px;
    width: 895px;
    height: 378px;
    background: var(--wall);
    box-shadow: 0 2px 10px rgba(3, 68, 87, 0.18);
  }
  .mural svg { display: block; width: 100%; height: 100%; }
  .tagline {
    font-family: "Montserrat", sans-serif;
    font-weight: 700;
    font-size: 76px;
  }
  .tagline--dark { fill: var(--teal); }
  .tagline--bronze { fill: var(--bronze); }
  .brand-name {
    font-family: "Montserrat", sans-serif;
    font-weight: 700;
    font-size: 108px;
    fill: var(--logo-text);
  }
</style>
</head>
<body>
<main class="canvas">
  <section class="mural" aria-label="VELO Hub selfie wall mural">
    <svg viewBox="0 0 1600 675" preserveAspectRatio="none" xmlns="http://www.w3.org/2000/svg">
      <defs>
        <linearGradient id="sweep-fill" gradientUnits="userSpaceOnUse" x1="760" y1="160" x2="900" y2="420">
          <stop offset="0" stop-color="var(--sweep-light)"/>
          <stop offset="0.35" stop-color="var(--sweep-mid)"/>
          <stop offset="0.65" stop-color="var(--sweep-cool)"/>
          <stop offset="1" stop-color="var(--teal)"/>
        </linearGradient>
      </defs>
      <rect class="wall-field" width="1600" height="675" fill="var(--wall)"/>

      <g class="color-sweep" role="img" aria-label="Decorative layered band sweeping from bronze into deep teal">
        <polygon fill="url(#sweep-fill)" points="30,675 790,185 1600,0 1600,675"/>
      </g>

      <text class="tagline tagline--dark" transform="translate(222 520) rotate(-32.8)" textLength="690" lengthAdjust="spacingAndGlyphs">LIVE · WORK ·</text>
      <text class="tagline tagline--bronze" transform="translate(815 168) rotate(-12.9)" textLength="480" lengthAdjust="spacingAndGlyphs">PLAY · GO</text>

      <g class="brand-lockup">
        <circle cx="968" cy="495" r="62" fill="var(--logo-dot)"/>
        <text class="brand-name" x="1085" y="534" textLength="380" lengthAdjust="spacingAndGlyphs">VELO</text>
      </g>
    </svg>
  </section>
</main>
</body>
</html>
```